Clinique VitaMira business card

I am looking for a talented designer who can an existing design and make it better. I need a 2 sided business card to represent our Psychology clinic staff members. It would need to be elegant, yet modern, clean, light and uplifting. Simple design, quick turnaround time. Lots of files and logos to use as your guide. I hope to hear from you!

Target Market(s)

Clients who receive the card of our therapists

Industry/Entity Type

Health And Wellness

Contact Information for Business Card

Following the similar designs of the Bluepine Care Center card, there will be 2 sides. Side 1 (front) should have the vitamira logo instead of the bluepine care logo, The title should read Clinique VitaMira instead of centre Soins Pinbleu/Bluepine care Center.

Side 2 should have a spiral similar to the one on the card with sunflower leaves, and the title of the Therapist should be Marie Lise Benkirane, Psychologue, Psychologist, her email: Marie@Vitamira-example.com and phone number should be (514) 555-0173

Font styles to use
Serif

Colors
fee18a
85cae6
ffffff
0255a3

Requirements
Must have
• Side 1 (front): vitamira logo- Name of the clinic, clinic address, contact info of clinic etc. use little icons in front of each (just like on sample card)
side 2: Therapist name titles and their contact info underneath with design of spiral and/or sunflower leaves..
Nice to have
• soft colors along soft yellow/gold and blue like the logo,
mini icons for phone, email, address etc.
We do work with a holistic, zen approach so it should represent that to some extent

```html
<!DOCTYPE html>
<html lang="fr">
<head>
<meta charset="utf-8">
<title>Clinique VitaMira – Business card</title>
<link href="https://fonts.googleapis.com/css2?family=Cormorant+Garamond:wght@500;600&family=Cormorant+SC:wght@600&display=swap" rel="stylesheet">
<style>
  :root {
    --page: #dedede;
    --paper: #f7f7f5;
    --navy: #23206b;
    --gold: #d5a514;
    --sun: #efd500;
    --sun-soft: #f4e58a;
  }
  * { box-sizing: border-box; margin: 0; padding: 0; }
  html, body { width: 1200px; height: 1200px; overflow: hidden; }
  body {
    background: var(--page);
    font-family: "Cormorant Garamond", Georgia, serif;
    color: var(--navy);
    position: relative;
  }
  .card {
    position: absolute;
    left: 250px;
    width: 700px;
    height: 400px;
    background: var(--paper);
    box-shadow: 0 6px 18px rgba(0,0,0,0.12);
    overflow: hidden;
  }
  .card--front { top: 150px; }
  .card--back { top: 650px; }

  /* Front */
  .brand {
    position: absolute;
    left: 60px; top: 150px;
    display: flex; align-items: center; gap: 14px;
  }
  .brand__dot {
    width: 34px; height: 34px; border-radius: 50%;
    background: var(--sun);
  }
  .brand__name {
    font-size: 60px; font-weight: 600; color: var(--navy); line-height: 1;
  }
  .divider {
    position: absolute;
    left: 390px; top: 70px;
    width: 1.5px; height: 260px;
    background: var(--sun-soft);
  }
  .clinic {
    position: absolute;
    left: 420px; top: 88px;
    width: 270px;
  }
  .clinic__title, .person__name {
    font-family: "Cormorant SC", Georgia, serif;
    font-weight: 600;
    color: var(--gold);
    letter-spacing: 1px;
  }
  .clinic__title { font-size: 25px; margin-bottom: 16px; }
  .contact { list-style: none; }
  .contact__item {
    display: flex; align-items: flex-start; gap: 10px;
    font-size: 18px; font-weight: 500; line-height: 1.2;
    margin-bottom: 9px;
  }
  .contact__item--phone { letter-spacing: 2.5px; font-size: 19px; }
  .icon { width: 16px; height: 16px; flex: none; margin-top: 2px; fill: var(--gold); }

  /* Back */
  .spiral-area {
    position: absolute;
    left: -90px; top: 30px;
    width: 430px; height: 430px;
    border-radius: 50%;
    background: radial-gradient(circle at 50% 50%, #fbf4c4 0%, var(--sun-soft) 45%, var(--sun) 70%, rgba(239,213,0,0) 71%);
  }
  .person {
    position: absolute;
    left: 380px; top: 120px;
  }
  .person__name { font-size: 28px; line-height: 1; }
  .person__role { font-size: 19px; font-weight: 500; margin: 2px 0 22px; }
  .person .contact__item { font-size: 21px; margin-bottom: 12px; }
  .person .contact__item--phone { letter-spacing: 1.5px; }
</style>
</head>
<body>

<section class="card card--front">
  <div class="brand">
    <span class="brand__dot"></span>
    <span class="brand__name">VitaMira</span>
  </div>
  <div class="divider"></div>
  <div class="clinic">
    <h1 class="clinic__title">Clinique VitaMira</h1>
    <ul class="contact">
      <li class="contact__item">
        <svg class="icon" viewBox="0 0 16 16"><path d="M8 0a5.5 5.5 0 0 0-5.5 5.5C2.5 9.5 8 16 8 16s5.5-6.5 5.5-10.5A5.5 5.5 0 0 0 8 0zm0 8a2.5 2.5 0 1 1 0-5 2.5 2.5 0 0 1 0 5z"/></svg>
        <span>480 rue des Érables<br>Laval, Qc., H7A 0B2</span>
      </li>
      <li class="contact__item contact__item--phone">
        <svg class="icon" viewBox="0 0 16 16"><path d="M3.6 1l2.3 3-1.3 1.6c.9 2 2.6 3.8 4.7 4.8l1.6-1.3 3 2.3-1.4 2.6C7.6 14 2 8.4 1 2.4z"/></svg>
        <span>514-555-0173</span>
      </li>
      <li class="contact__item">
        <svg class="icon" viewBox="0 0 16 16"><path d="M1 3h14v10H1z"/><path d="M1 3l7 6 7-6" fill="none" stroke="#f7f7f5" stroke-width="1.4"/></svg>
        <span>info@vitamira-example.com</span>
      </li>
      <li class="contact__item">
        <svg class="icon" viewBox="0 0 16 16"><circle cx="8" cy="8" r="7" fill="none" stroke="#d5a514" stroke-width="1.6"/><path d="M1 8h14M8 1c-3 4-3 10 0 14M8 1c3 4 3 10 0 14" fill="none" stroke="#d5a514" stroke-width="1.2"/></svg>
        <span>www.vitamira-example.com</span>
      </li>
      <li class="contact__item">
        <svg class="icon" viewBox="0 0 16 16"><circle cx="8" cy="8" r="7"/></svg>
        <span>www.social-example.com/VitaMira</span>
      </li>
    </ul>
  </div>
</section>

<section class="card card--back">
  <div class="spiral-area" role="img" aria-label="Large soft yellow spiral decoration"></div>
  <div class="person">
    <h2 class="person__name">Marie Lise Benkirane</h2>
    <p class="person__role">Psychologue, Psychologist</p>
    <ul class="contact">
      <li class="contact__item contact__item--phone">
        <svg class="icon" viewBox="0 0 16 16"><rect x="4" y="1" width="8" height="14" rx="1.5" fill="none" stroke="#d5a514" stroke-width="1.4"/></svg>
        <span>(514) 555-0173</span>
      </li>
      <li class="contact__item">
        <svg class="icon" viewBox="0 0 16 16"><path d="M1 3h14v10H1z"/><path d="M1 3l7 6 7-6" fill="none" stroke="#f7f7f5" stroke-width="1.4"/></svg>
        <span>Marie@Vitamira-example.com</span>
      </li>
    </ul>
  </div>
</section>

</body>
</html>
```